cosmetic business needs inner and outer packaging

We, Velisto cosmetics, are a importer and oline retail of beauty products on an argan oil base. We will put 2 new products on the market.
A glass bottle 50ml of pure oil, and a 150g jar facemask.
Both need inner and outter packaging design.

Dimension of packaging:
Face mask jar:
- width : 20 cm - Height : 3 cm
Outter packaging:
- Width :  7,7 cm - height :  6,3 cm

Oil Bottle:
-Width : 10,4 cm - height : 4,3 cm
Outer packaging:
- Width :  3,8 cm - height :  12 cm

Pictures of the Jar & bottle are attached.

Our Brand:
Velisto design sources its products directly from the cooperatives in Morocco. The coorperatives are run by the local women. Therefore we support the local economy, independence of the woman and sustainable production.
We offer two classic beauty products. The pure argan oil, can be used for hair, skin or nails. It comes in a 50ml blue glass bottle.
A ghassoul face mask, comes in a jar of 150g.

For the design we envision a classicm, timeless design. Colours like lavendel, burgundy or indigo with specks of silver or gold. On the right side of the outter package we imagine an outline of what is inside. So a sillhouette of the jar/bottle.(see attached picture) But these are only ideas not limitations.
Attached some pictures of competitors.
If possible i would like to be able to amend the text as there cna be changes.

some competitors:
http://www.plumerin.co.uk/
http://www.kestrabow.co.uk/03_face_oil.html
https://orvinellu.com/

aldo obviously the logo has to be incoorperated in the packaging, so the bonus in the end will not demand any extra work

Target Market(s)

Taget marked:
Manily women, 26+ years, urban, interested in social and enviromental issues, earing money and able to spend on luxury products, interest in cosmetics,

Industry/Entity Type

Cosmetics

Logo Text

Velisto

Requirements
Must have
• amendable text on the back, as there are some legal requirements for cosmetic products.

```html
<!DOCTYPE html>
<html lang="en">
<head>
<meta charset="utf-8">
<title>Velisto cosmetics – Argan Oil packaging</title>
<link rel="stylesheet" href="https://fonts.googleapis.com/css2?family=Cinzel:wght@700&family=Josefin+Sans:wght@400;600&family=Libre+Baskerville&display=swap">
<style>
  :root {
    --bg-top: #f1f2f4;
    --bg-bottom: #ffffff;
    --navy: #132247;
    --navy-deep: #0d1936;
    --jar-blue: #1a2d6e;
    --bottle-blue: #1f33a8;
    --silver: #d3d6dc;
    --silver-dim: #8f97ab;
    --ornament: #2a3a63;
  }
  html, body { margin: 0; padding: 0; overflow: hidden; }
  .canvas {
    position: relative;
    width: 1200px;
    height: 754px;
    overflow: hidden;
    background: linear-gradient(180deg, var(--bg-top) 0%, var(--bg-bottom) 45%);
    font-family: "Josefin Sans", sans-serif;
    color: var(--silver);
  }
  .panel {
    position: absolute;
    background: var(--navy);
    box-sizing: border-box;
    overflow: hidden;
  }
  .ornament {
    position: absolute;
    border-radius: 50%;
    background: radial-gradient(circle, var(--ornament) 0%, rgba(42,58,99,0.55) 45%, rgba(42,58,99,0) 70%);
  }
  .brand {
    position: absolute;
    left: 0; right: 0;
    display: flex;
    flex-direction: column;
    align-items: center;
    gap: 6px;
  }
  .brand-dot {
    width: 26px; height: 26px;
    border-radius: 50%;
    border: 2px solid var(--silver);
    box-sizing: border-box;
  }
  .brand-name {
    font-family: "Josefin Sans", sans-serif;
    font-weight: 400;
    text-transform: uppercase;
    letter-spacing: 0.04em;
    color: var(--silver);
  }
  .product {
    position: absolute;
    left: 0; right: 0;
    text-align: center;
    font-family: "Cinzel", serif;
    font-weight: 700;
    color: var(--silver);
    line-height: 1;
  }
  .product small { display: block; }
  .claim {
    position: absolute;
    left: 0; right: 0;
    text-align: center;
    font-family: "Libre Baskerville", serif;
    color: var(--silver);
  }
  .claim strong { display: block; font-family: "Cinzel", serif; font-weight: 700; }
  .claim span { display: block; text-transform: uppercase; }
  .side-copy {
    position: absolute;
    font-family: "Libre Baskerville", serif;
    color: var(--silver-dim);
    line-height: 1.45;
  }

  /* Face mask outer box */
  .mask-box-side { left: 40px; top: 300px; width: 110px; height: 250px; background: var(--navy-deep); }
  .mask-box-side .side-copy { left: 10px; right: 10px; top: 18px; font-size: 7.5px; }
  .mask-box-side .mini-brand { position: absolute; left: 0; right: 0; top: 170px; display: flex; flex-direction: column; align-items: center; gap: 3px; }
  .mask-box-side .mini-brand .brand-dot { width: 12px; height: 12px; border-width: 1px; }
  .mask-box-side .mini-brand .brand-name { font-size: 6px; }
  .mask-box-side .ingredients { position: absolute; left: 0; right: 0; top: 205px; text-align: center; font-family: "Libre Baskerville", serif; font-size: 6.5px; color: var(--silver-dim); }
  .mask-box-front { left: 150px; top: 300px; width: 250px; height: 250px; }
  .mask-box-front .ornament.a { width: 220px; height: 220px; right: -110px; top: -30px; }
  .mask-box-front .ornament.b { width: 200px; height: 200px; left: -110px; bottom: -90px; }
  .mask-box-front .brand { top: 40px; }
  .mask-box-front .brand-name { font-size: 11px; }
  .mask-box-front .product { top: 150px; font-size: 22px; }
  .mask-box-front .product small { font-size: 13px; margin-bottom: 4px; }
  .mask-box-front .claim { top: 210px; font-size: 6.5px; }
  .mask-box-front .claim strong { font-size: 9px; margin-bottom: 3px; }

  /* Jar label */
  .jar-label { left: 430px; top: 320px; width: 270px; height: 180px; background: var(--jar-blue); border-radius: 4px; }
  .jar-label .ornament.a { width: 200px; height: 200px; left: -100px; top: -60px; }
  .jar-label .ornament.b { width: 200px; height: 200px; right: -100px; bottom: -80px; }
  .jar-label .brand { top: 18px; }
  .jar-label .brand-name { font-size: 9px; }
  .jar-label .product { top: 76px; font-size: 22px; }
  .jar-label .product small { font-size: 13px; margin-bottom: 4px; }
  .jar-label .claim { top: 136px; font-size: 6.5px; }
  .jar-label .claim strong { font-size: 10px; margin-bottom: 3px; }

  /* Bottle label */
  .bottle-label { left: 740px; top: 330px; width: 130px; height: 180px; background: var(--navy); }
  .bottle-label .ornament.a { width: 170px; height: 170px; left: -20px; top: 10px; }
  .bottle-label .brand { top: 16px; gap: 4px; }
  .bottle-label .brand-dot { width: 18px; height: 18px; }
  .bottle-label .brand-name { font-size: 6.5px; }
  .bottle-label .product { top: 88px; font-size: 20px; }
  .bottle-label .claim { top: 140px; font-size: 4.5px; }
  .bottle-label .claim strong { font-size: 8px; margin-bottom: 2px; }

  /* Oil outer box */
  .oil-box-front { left: 900px; top: 150px; width: 170px; height: 420px; }
  .oil-box-front .ornament.a { width: 230px; height: 230px; left: -10px; top: 150px; }
  .oil-box-front .brand { top: 45px; }
  .oil-box-front .brand-name { font-size: 10px; }
  .oil-box-front .product { top: 255px; font-size: 30px; }
  .oil-box-front .claim { top: 345px; font-size: 5.5px; }
  .oil-box-front .claim strong { font-size: 10px; margin-bottom: 3px; }
  .oil-box-front .volume { position: absolute; left: 0; right: 0; top: 385px; text-align: center; font-size: 11px; color: var(--silver); }
  .oil-box-side { left: 1070px; top: 150px; width: 70px; height: 420px; background: var(--navy-deep); }
  .oil-box-side .side-copy { left: 8px; right: 8px; top: 90px; font-size: 7px; }
  .oil-box-side .ingredients { position: absolute; left: 8px; right: 8px; top: 300px; font-family: "Libre Baskerville", serif; font-size: 6.5px; color: var(--silver-dim); }
  .oil-box-side .ornament.a { width: 120px; height: 120px; left: -60px; top: 170px; }
</style>
</head>
<body>
<main class="canvas">

  <section class="panel mask-box-side" aria-label="Face mask box side panel">
    <p class="side-copy">Gentle ghassoul clay blended with pure argan oil cleanses, softens and restores the skin. Apply to clean face, leave ten minutes, rinse with warm water.</p>
    <div class="mini-brand"><span class="brand-dot"></span><span class="brand-name">Velisto cosmetics</span></div>
    <p class="ingredients">Ingredients:<br>100% Argan Oil</p>
  </section>

  <section class="panel mask-box-front" aria-label="Face mask box front panel">
    <div class="ornament a" role="img" aria-label="Silver mandala ornament"></div>
    <div class="ornament b" role="img" aria-label="Silver mandala ornament"></div>
    <div class="brand"><span class="brand-dot"></span><span class="brand-name">Velisto cosmetics</span></div>
    <h2 class="product"><small>Argan Oil</small>Face Mask</h2>
    <p class="claim"><strong>Organic</strong><span>For all skin types</span></p>
  </section>

  <section class="panel jar-label" aria-label="Face mask jar label">
    <div class="ornament a" role="img" aria-label="Silver mandala ornament"></div>
    <div class="ornament b" role="img" aria-label="Silver mandala ornament"></div>
    <div class="brand"><span class="brand-dot"></span><span class="brand-name">Velisto cosmetics</span></div>
    <h2 class="product"><small>Argan Oil</small>Face Mask</h2>
    <p class="claim"><strong>Organic</strong><span>For all skin types</span></p>
  </section>

  <section class="panel bottle-label" aria-label="Argan oil bottle label">
    <div class="ornament a" role="img" aria-label="Silver mandala ornament"></div>
    <div class="brand"><span class="brand-dot"></span><span class="brand-name">Velisto cosmetics</span></div>
    <h2 class="product">Argan<br>Oil</h2>
    <p class="claim"><strong>Organic</strong><span>For all skin and hair types</span></p>
  </section>

  <section class="panel oil-box-front" aria-label="Argan oil box front panel">
    <div class="ornament a" role="img" aria-label="Silver mandala ornament"></div>
    <div class="brand"><span class="brand-dot"></span><span class="brand-name">Velisto cosmetics</span></div>
    <h2 class="product">Argan<br>Oil</h2>
    <p class="claim"><strong>Organic</strong><span>For all skin and hair types</span></p>
    <p class="volume">50ml</p>
  </section>

  <section class="panel oil-box-side" aria-label="Argan oil box side panel">
    <div class="ornament a" role="img" aria-label="Silver mandala ornament"></div>
    <p class="side-copy">Cold pressed argan oil sourced from women's cooperatives in southwestern Morocco. Nourishes skin, hair and nails.</p>
    <p class="ingredients">Ingredients:<br>100% Argan Oil</p>
  </section>

</main>
</body>
</html>
```